Investment Fund Investor newsletter

I deleted the tear sheet example which was provided for design purposes only and not for content. Please see the simple outline for the newsletter and the related sections.

Please be clear this project is for a newsletter template. This means a template that can be updated on a monthly or quarterly basis with new content for our audience. Sections should include: Operations Update, Financial Update, Energy Investor News.

We need a template for a newsletter that can be sent out in Word format and also able to send out via Mailchimp. Audience are current investors in our oil and gas fund. These investors are high net worth individuals and private equity firms so the branding needs to be high end, sophisticated and corporate. Please see website and attached tear sheet for the type of branding that we want to match. Website is www.brambleford-power.com
Please see website and tear sheet for the color scheme that we want.

Target Market(s)

Our current fund investors that include high net worth investors and CEOs of private equity companies

Industry/Entity Type

oil and gas... investment

Font styles to use
Serif

Requirements
Must have
• Word file and can send via Mailchimp too

```html
<!DOCTYPE html>
<html lang="en">
<head>
<meta charset="utf-8">
<title>Brambleford Power Partners II: LP Update</title>
<link rel="stylesheet" href="https://fonts.googleapis.com/css2?family=Merriweather:ital,wght@1,700&family=Inter:wght@400;600&display=swap">
<style>
  :root {
    --desk: #e6e6e6;
    --paper: #ffffff;
    --ink: #1a1a1a;
    --heading: #2b2b2b;
    --accent: #00a8e8;
    --link: #1f5fbf;
    --rule: #b5b5b5;
    --white: #ffffff;
    --sunset-top: #3a1a0c;
    --sunset-mid: #c5461a;
    --sunset-low: #1c0d08;
    --pipe-dark: #1c1816;
    --pipe-rust: #6b4a2e;
  }
  * { box-sizing: border-box; margin: 0; padding: 0; }
  html, body { width: 1200px; height: 771px; overflow: hidden; background: var(--desk); }
  body { position: relative; font-family: "Inter", Arial, sans-serif; color: var(--ink); }

  .page {
    position: absolute; top: 4px; width: 587px; height: 761px;
    background: var(--paper); border: 1px solid #c9c9c9; overflow: hidden;
  }
  .page--front { left: 6px; }
  .page--back { left: 607px; }

  .masthead {
    position: absolute; left: 0; top: 0; width: 100%; height: 136px;
    background: linear-gradient(180deg, var(--sunset-top) 0%, var(--sunset-mid) 55%, var(--sunset-low) 100%);
  }
  .brand {
    position: absolute; display: flex; align-items: center; gap: 5px;
    font-family: "Merriweather", Georgia, serif; font-style: italic; font-weight: 700;
    color: var(--white); letter-spacing: .5px;
  }
  .brand__mark { width: 9px; height: 9px; background: var(--white); }
  .masthead .brand { left: 22px; top: 46px; font-size: 9px; }
  .masthead__title {
    position: absolute; left: 0; right: 0; top: 72px; text-align: center;
    font-family: "Merriweather", Georgia, serif; font-style: italic; font-weight: 700;
    font-size: 17px; color: var(--white);
  }
  .masthead__issue {
    position: absolute; left: 0; right: 0; top: 104px; text-align: center;
    font-family: "Merriweather", Georgia, serif; font-style: italic; font-weight: 700;
    font-size: 12.5px; color: var(--white);
  }

  .section { position: absolute; left: 69px; width: 445px; }
  .section__head { position: relative; height: 58px; }
  .section__icon { position: absolute; left: 5px; top: 0; width: 50px; height: 50px; }
  .section__title {
    position: absolute; left: 75px; top: 6px;
    font-family: "Merriweather", Georgia, serif; font-style: italic; font-weight: 700;
    font-size: 15px; color: var(--heading);
  }
  .section__bar { position: absolute; left: 79px; top: 38px; width: 39px; height: 4px; background: var(--accent); }
  .section__body p { font-size: 11.6px; line-height: 15.2px; margin-bottom: 6px; }
  .section__body p + p + p { margin-top: 10px; }

  .section--ops { top: 166px; }
  .section--fin { top: 446px; }

  .divider { position: absolute; left: 110px; top: 413px; width: 371px; height: 12px; }
  .divider::before, .divider::after {
    content: ""; position: absolute; top: 6px; width: 161px; height: 1.5px; background: var(--rule);
  }
  .divider::before { left: 0; }
  .divider::after { right: 0; }
  .divider__mark { position: absolute; left: 180px; top: 0; width: 12px; height: 12px; background: var(--rule); }

  .section--news { top: 64px; left: 72px; width: 470px; }
  .news-list { list-style: none; margin-top: 26px; }
  .news-list li { font-size: 11.6px; line-height: 15px; margin-bottom: 8px; }
  .news-list a { color: var(--link); text-decoration: underline; }

  .contact {
    position: absolute; left: 0; bottom: 0; width: 100%; height: 157px;
    background: linear-gradient(100deg, var(--pipe-dark) 0%, var(--pipe-rust) 45%, var(--pipe-dark) 70%, var(--pipe-rust) 100%);
    color: var(--white);
  }
  .contact__title {
    position: absolute; left: 59px; top: 26px;
    font-family: "Merriweather", Georgia, serif; font-style: italic; font-weight: 700; font-size: 17px;
  }
  .contact__lines { position: absolute; left: 59px; top: 60px; list-style: none; }
  .contact__lines li { font-size: 11.6px; font-weight: 600; line-height: 19px; }
  .contact .brand { right: 28px; top: 94px; font-size: 14px; }
  .contact .brand__mark { width: 12px; height: 12px; }
</style>
</head>
<body>

<article class="page page--front">
  <header class="masthead" role="img" aria-label="Photograph of oil pumpjacks silhouetted against an orange sunset">
    <div class="brand"><span class="brand__mark"></span>Brambleford Power Partners</div>
    <h1 class="masthead__title">Brambleford Power Partners II: LP Update</h1>
    <p class="masthead__issue">Q4 2022 Update</p>
  </header>

  <section class="section section--ops">
    <div class="section__head">
      <svg class="section__icon" viewBox="0 0 50 50" fill="none" stroke="#1a1a1a" stroke-width="1.6">
        <circle cx="25" cy="25" r="7"/>
        <path d="M25 10l3 0 1 4 4 2 4-2 2 2-2 4 2 4 4 1 0 3 0 3-4 1-2 4 2 4-2 2-4-2-4 2-1 4-3 0-3 0-1-4-4-2-4 2-2-2 2-4-2-4-4-1 0-3 0-3 4-1 2-4-2-4 2-2 4 2 4-2 1-4z"/>
        <path d="M8 17a19 19 0 0 1 9-9M42 33a19 19 0 0 1-9 9"/>
        <path d="M17 8l0 3-3 0M33 42l0-3 3 0"/>
      </svg>
      <h2 class="section__title">Operations Update</h2>
      <span class="section__bar"></span>
    </div>
    <div class="section__body">
      <p>Nemo enim ipsam voluptatem, quia voluptas sit, aspernatur aut odit aut fugit, sed quia consequuntur magni dolores eos, qui ratione voluptatem sequi nesciunt, neque porro quisquam est, qui dolorem ipsum, quia dolor sit amet consectetur adipisci velit, sed quia non numquam eius modi tempora incidunt, ut labore et dolore magnam aliquam quaerat voluptatem.</p>
      <p>Ut enim ad minima veniam, quis nostrum exercitationem ullam corporis suscipit laboriosam, nisi ut aliquid ex ea commodi consequatur?</p>
      <p>Quis autem vel eum iure reprehenderit, qui in ea voluptate velit esse, quam nihil molestiae consequatur, vel illum, qui dolorem eum fugiat, quo voluptas nulla pariatur?</p>
    </div>
  </section>

  <div class="divider"><span class="divider__mark"></span></div>

  <section class="section section--fin">
    <div class="section__head">
      <svg class="section__icon" viewBox="0 0 50 50" fill="none" stroke="#1a1a1a" stroke-width="1.6">
        <rect x="4" y="4" width="42" height="30"/>
        <path d="M25 34v4M25 38l-10 10M25 38l10 10"/>
        <path d="M9 11h10M9 15h7M9 19h12"/>
        <path d="M10 30l9-8 6 4 13-12"/>
        <path d="M33 14h5v5"/>
      </svg>
      <h2 class="section__title">Financial Update</h2>
      <span class="section__bar"></span>
    </div>
    <div class="section__body">
      <p>Nemo enim ipsam voluptatem, quia voluptas sit, aspernatur aut odit aut fugit, sed quia consequuntur magni dolores eos, qui ratione voluptatem sequi nesciunt, neque porro quisquam est, qui dolorem ipsum, quia dolor sit amet consectetur adipisci velit, sed quia non numquam eius modi tempora incidunt, ut labore et dolore magnam aliquam quaerat voluptatem.</p>
      <p>Ut enim ad minima veniam, quis nostrum exercitationem ullam corporis suscipit laboriosam, nisi ut aliquid ex ea commodi consequatur?</p>
      <p>Quis autem vel eum iure reprehenderit, qui in ea voluptate velit esse, quam nihil molestiae consequatur, vel illum, qui dolorem eum fugiat, quo voluptas nulla pariatur?</p>
    </div>
  </section>
</article>

<article class="page page--back">
  <section class="section section--news">
    <div class="section__head">
      <svg class="section__icon" viewBox="0 0 50 50" fill="none" stroke="#1a1a1a" stroke-width="1.6">
        <path d="M12 4h34v40a4 4 0 0 1-4 4H8a4 4 0 0 1-4-4V14h8"/>
        <path d="M12 4v40a4 4 0 0 1-4 4"/>
        <path d="M8 16v28"/>
        <rect x="17" y="10" width="24" height="9"/>
        <path d="M17 24h24M17 28h24M17 32h11M17 36h11M17 40h11"/>
        <rect x="31" y="32" width="10" height="8"/>
      </svg>
      <h2 class="section__title">Energy Investor News</h2>
      <span class="section__bar"></span>
    </div>
    <ul class="news-list">
      <li><a href="#">Will the Producers' Group Cut Production on Labor Day?</a> (crudewire.net)</li>
      <li><a href="#">Harlan Ames Keeps Betting Big on Oil</a> (Harbor Finance)</li>
      <li><a href="#">What is Behind Wall Street’s $100 oil Forecast?</a> (Daily Ledger)</li>
    </ul>
  </section>

  <footer class="contact" role="img" aria-label="Photograph of stacked rusty steel drill pipes">
    <h2 class="contact__title">Contact Us</h2>
    <ul class="contact__lines">
      <li>Our Address</li>
      <li>(555) 014-2290</li>
      <li>info@brambleford-power.com</li>
    </ul>
    <div class="brand"><span class="brand__mark"></span>Brambleford Power</div>
  </footer>
</article>

</body>
</html>
```